Flyer DesignFESTIVE, FLORISTRY WORKSHOP

WE NEED A FLYER, TO SEND OUT TO PROSPECTIVE CUSTOMERS, TO ATTEND A ONE DAY CHRISTMAS WORKSHOP, ALL MATERIALS WILL BE SUPPLIED AND SO TO WE WILL PROVIDE REFRESHMENTS, PARTICIPIANTS JUST NEED TO BRING THIER FLORISTRY SCISSORS

ON THE DAY THE WILL PARTICIPIATE IN CREATING SEASONAL FLORISTRY DESIGNS THAT THEY CAN BRING HOME TO LAST THE FESTIVE SEASON,

MAREIKE AND LORNA WILL BE THERE WITH SOME UNIQUE IDEAS TO ENHANCE OUR CHRISTMAS FESTIVITIES. TOTAL COST FOR THE DAY IS £79.00. AND THE DATE IS 6THDECEMBER, 2014, AT THE BRAMBLEGATE HOTEL DUNMARREN, WHICH HAS ALSO A BUS LINK TO MANY OTHER AREAS, SO ENJOY YOURSELVES, GET INTO THE FESTIVE FEELING ON THIS SPECIAL OCCASION

FLOWER LOVERS THAT LIKE TO CREATE THIER OWN FLORAL DESIGNS

Hotel

Decorative

Must have
• A CHRISTMAS ATMOSPHERE, WITH A BEAUTIFUL DOOR WREATH AND TABLE DESIGN

BOTH TUTORS ON THE DAY ARE HIGHLY SKILLED, HIGHLY QUALIFIED, WITH LORNA, HAVING WON GFA WEXLEY MEDAL,
Nice to have
• BETTER WORDING THAN I HAVE GIVEN YOU

telephone number 02894412385

```html
<!DOCTYPE html>
<html lang="en">
<head>
<meta charset="utf-8">
<title>One Day Seasonal Floristry Christmas Workshop</title>
<link rel="stylesheet" href="https://fonts.googleapis.com/css2?family=Playball&family=Cinzel:wght@600&family=EB+Garamond:wght@400;600&display=swap">
<style>
  :root {
    --stage: #2b2b2b;
    --paper-light: #f7f7f5;
    --paper-shade: #e4e4e2;
    --gold-dark: #7a5c14;
    --gold: #a8842e;
    --gold-light: #e0bf62;
    --red: #b3181d;
    --red-bright: #d4222a;
    --ink: #2a2a2a;
    --white: #ffffff;
  }
  html, body {
    margin: 0;
    padding: 0;
    width: 1200px;
    height: 907px;
    overflow: hidden;
    background: var(--stage);
  }
  .flyer {
    position: absolute;
    left: 45px;
    top: 62px;
    width: 1110px;
    height: 785px;
    overflow: hidden;
    background: radial-gradient(ellipse at 60% 40%, var(--paper-light) 0%, var(--paper-shade) 100%);
  }
  .flyer-art {
    position: absolute;
    inset: 0;
    width: 1110px;
    height: 785px;
  }
  .title {
    position: absolute;
    right: 36px;
    top: 26px;
    margin: 0;
    text-align: right;
    font-family: "Playball", cursive;
    font-weight: 400;
    font-size: 60px;
    line-height: 76px;
    color: var(--gold);
    background: linear-gradient(180deg, var(--gold-dark) 0%, var(--gold-light) 50%, var(--gold-dark) 100%);
    -webkit-background-clip: text;
    background-clip: text;
    -webkit-text-fill-color: transparent;
  }
  .title .line { display: block; }
  .tutors {
    position: absolute;
    right: 40px;
    top: 208px;
    margin: 0;
    font-family: "Cinzel", serif;
    font-weight: 600;
    font-size: 44px;
    letter-spacing: 2px;
    color: var(--red);
  }
  .intro {
    position: absolute;
    right: 36px;
    top: 276px;
    margin: 0;
    text-align: right;
    font-family: "EB Garamond", serif;
    font-size: 22.5px;
    line-height: 31px;
    color: var(--ink);
  }
  .intro .line { display: block; white-space: nowrap; }
  .date {
    position: absolute;
    right: 32px;
    top: 424px;
    margin: 0;
    font-family: "EB Garamond", serif;
    font-weight: 600;
    font-size: 47px;
    line-height: 56px;
    color: var(--gold);
  }
  .venue {
    position: absolute;
    right: 32px;
    top: 482px;
    margin: 0;
    font-family: "EB Garamond", serif;
    font-size: 37px;
    line-height: 44px;
    color: var(--gold);
  }
  .note {
    position: absolute;
    right: 30px;
    top: 536px;
    margin: 0;
    text-align: center;
    font-family: "EB Garamond", serif;
    font-size: 17px;
    line-height: 23px;
    color: var(--ink);
  }
  .note .line { display: block; white-space: nowrap; }
  .price-badge {
    position: absolute;
    left: 906px;
    top: 596px;
    width: 166px;
    height: 166px;
    border-radius: 50%;
    background: radial-gradient(circle at 40% 35%, var(--red-bright) 0%, var(--red) 80%);
    border: 5px solid var(--white);
    box-shadow: 0 3px 8px rgba(0,0,0,0.35);
    color: var(--white);
    text-align: center;
    font-family: "EB Garamond", serif;
    box-sizing: border-box;
  }
  .price-amount {
    display: block;
    margin-top: 24px;
    font-size: 66px;
    line-height: 64px;
  }
  .price-term {
    display: block;
    font-size: 16px;
    letter-spacing: 1px;
  }
</style>
</head>
<body>
  <main class="flyer">
    <svg class="flyer-art" viewBox="0 0 1110 785" xmlns="http://www.w3.org/2000/svg">
      <defs>
        <linearGradient id="gold-sheen" x1="0" y1="0" x2="1" y2="1">
          <stop offset="0" stop-color="#a7801f"/>
          <stop offset="0.45" stop-color="#f0d271"/>
          <stop offset="1" stop-color="#b8901f"/>
        </linearGradient>
        <linearGradient id="table-red" x1="0" y1="0" x2="0" y2="1">
          <stop offset="0" stop-color="#e0313a"/>
          <stop offset="1" stop-color="#b0141b"/>
        </linearGradient>
        <radialGradient id="wreath-tones" cx="0.5" cy="0.5" r="0.5">
          <stop offset="0" stop-color="#7d4a3a" stop-opacity="0.85"/>
          <stop offset="0.6" stop-color="#3f7a3c" stop-opacity="0.85"/>
          <stop offset="1" stop-color="#3f7a3c" stop-opacity="0"/>
        </radialGradient>
        <radialGradient id="centrepiece-tones" cx="0.5" cy="0.5" r="0.5">
          <stop offset="0" stop-color="#6f8f4e" stop-opacity="0.95"/>
          <stop offset="0.6" stop-color="#3f7f34" stop-opacity="0.9"/>
          <stop offset="1" stop-color="#3f7f34" stop-opacity="0"/>
        </radialGradient>
      </defs>

      <path class="table-band" d="M120,645 L1110,645 L1110,785 L150,785 C110,740 105,690 120,645 Z" fill="url(#table-red)"/>

      <path class="swoosh-top" d="M0,0 L390,0 C260,18 110,55 0,138 Z" fill="url(#gold-sheen)"/>
      <path class="swoosh-top-edge" d="M390,0 C260,18 110,55 0,138" fill="none" stroke="#ffffff" stroke-width="6"/>

      <path class="swoosh-left" d="M0,225 C150,300 265,420 245,565 C228,680 110,735 215,785 L0,785 Z" fill="url(#gold-sheen)"/>
      <path class="swoosh-left-edge" d="M0,225 C150,300 265,420 245,565 C228,680 110,735 215,785" fill="none" stroke="#ffffff" stroke-width="8"/>

      <rect class="wreath-photo" x="20" y="28" width="360" height="340" fill="url(#wreath-tones)" role="img" aria-label="Photograph of an evergreen Christmas door wreath with red poinsettias and a red bow"/>

      <rect class="centrepiece-photo" x="140" y="520" width="480" height="265" fill="url(#centrepiece-tones)" role="img" aria-label="Photograph of a table centrepiece of fir greenery, pine cones and two white pillar candles"/>
    </svg>

    <h1 class="title">
      <span class="line">One Day Seasonal Floristry</span>
      <span class="line">Christmas Workshop</span>
    </h1>

    <h2 class="tutors">MAREIKE AND LORNA</h2>

    <p class="intro">
      <span class="line">a highly skilled, highly qualified tutors will run the workshop</span>
      <span class="line">with some unique ideas to enhance our Christmas Festivities.</span>
      <span class="line">Participate in creating seasonal floristry design and</span>
      <span class="line">bring home to last the festive season</span>
    </p>

    <p class="date">6th December, 2014</p>
    <p class="venue">Bramblegate Hotel Dunmarren</p>
    <p class="note">
      <span class="line">All materials will be supplied. Participants need to bring</span>
      <span class="line">their floristry scissors only.</span>
    </p>

    <div class="price-badge">
      <span class="price-amount">£79</span>
      <span class="price-term">FOR THE DAY</span>
    </div>
  </main>
</body>
</html>
```